Geschäftspapiere für gemeinnützige Organisation im weltweiten Bildungsbereich
Zielgruppe
Wir sind eine gemeinnützige Organisation mit Projekten im Bildungsbereich weltweit. Unsere Zielgruppe sind andere gemeinnützige Organisationen und Studenten.
Aufgabenstellung
Das Logo sollte aud das Geschäftspapier sowie änhnliche Farben bei den Informationen genutzt werden (orange und/ oder grün).
KLT Berlin gemeinnützige GmbH
Falkenhainer Weg 14, D-12489 Berlin
www.klt-bildung.example I Geschäftsführer: Jorinde Paskova, Lukas Drömberg I Amtsgericht Berlin-Charlottenburg, HRB 417592 B

```html
<!DOCTYPE html>
<html lang="de">
<head>
<meta charset="utf-8">
<title>KLT Berlin – Briefpapier</title>
<link href="https://fonts.googleapis.com/css2?family=Lato:wght@400;700&family=Arimo:wght@400&display=swap" rel="stylesheet">
<style>
  :root {
    --orange: #e4672a;
    --orange-mid: #f28c28;
    --orange-light: #fbb97c;
    --green: #a2c93a;
    --text: #111111;
    --grey: #555555;
    --paper: #ffffff;
    --backdrop: #efefef;
    --watermark: #f1f1f1;
  }
  html, body {
    margin: 0;
    padding: 0;
    width: 1200px;
    height: 3000px;
    overflow: hidden;
    background: var(--backdrop);
  }
  .letter {
    position: absolute;
    left: 100px;
    top: 793px;
    width: 1000px;
    height: 1414px;
    background: var(--paper);
    box-shadow: 0 4px 14px rgba(0,0,0,0.18);
    overflow: hidden;
    font-family: "Lato", sans-serif;
    color: var(--grey);
  }
  .stripe { position: absolute; left: 0; width: 25px; }
  .stripe--light { top: 0; height: 500px; background: var(--orange-light); }
  .stripe--mid { top: 500px; height: 207px; background: var(--orange-mid); }
  .stripe--green { top: 707px; height: 292px; background: var(--green); }
  .corner-band {
    position: absolute; right: 0; top: 0;
    width: 23px; height: 213px; background: var(--orange);
  }
  .brand {
    position: absolute; left: 119px; top: 120px;
    display: flex; align-items: center; gap: 22px;
  }
  .brand__mark { width: 74px; height: 74px; background: var(--orange-mid); }
  .brand__name {
    font-family: "Lato", sans-serif; font-weight: 700;
    font-size: 46px; color: var(--orange); letter-spacing: 2px;
  }
  .company {
    position: absolute; right: 48px; top: 170px;
    text-align: right; font-size: 20px; line-height: 23px;
  }
  .company__name { color: var(--orange); }
  .company__address { color: var(--grey); }
  .company__address svg { vertical-align: -2px; margin-right: 6px; }
  .sender-line {
    position: absolute; left: 119px; top: 267px;
    font-size: 11.5px; color: var(--grey);
  }
  .sender-line span { color: var(--orange); }
  .memo {
    position: absolute; left: 119px; top: 297px;
    font-size: 17px; line-height: 25.5px; color: var(--text);
  }
  .memo__row { display: flex; }
  .memo__label { width: 62px; font-weight: 700; }
  .body-copy {
    position: absolute; left: 119px; top: 541px; width: 786px;
    font-family: "Arimo", sans-serif; font-size: 18.3px; line-height: 22.2px;
    color: var(--text); text-align: justify;
  }
  .body-copy p { margin: 0 0 22.2px; }
  .watermark {
    position: absolute; left: 610px; top: 1110px;
    width: 420px; height: 420px; border-radius: 50%;
    background: var(--watermark);
  }
  .footer-col {
    position: absolute; top: 1298px; height: 78px;
    border-left: 2px solid var(--green);
    padding-left: 16px; padding-top: 14px;
    font-size: 15.5px; line-height: 18px; color: var(--grey);
    box-sizing: border-box;
  }
  .footer-col--contact { left: 119px; padding-left: 20px; }
  .footer-col--management { left: 384px; }
  .footer-col--register { left: 649px; }
  .footer-col__title { color: var(--green); }
  .contact-row { display: flex; align-items: center; gap: 8px; }
  .contact-row svg { width: 11px; height: 11px; }
</style>
</head>
<body>
  <div class="letter">
    <div class="stripe stripe--light"></div>
    <div class="stripe stripe--mid"></div>
    <div class="stripe stripe--green"></div>
    <div class="corner-band"></div>

    <div class="brand">
      <div class="brand__mark"></div>
      <div class="brand__name">KLT BERLIN</div>
    </div>

    <div class="company">
      <div class="company__name">KLT Berlin gemeinnützige GmbH</div>
      <div class="company__address"><svg width="12" height="16" viewBox="0 0 12 16"><path d="M6 0a6 6 0 0 0-6 6c0 4.5 6 10 6 10s6-5.5 6-10a6 6 0 0 0-6-6zm0 8.5A2.5 2.5 0 1 1 6 3.5a2.5 2.5 0 0 1 0 5z" fill="#e4672a"/></svg>Falkenhainer Weg 14, D-12489 Berlin</div>
    </div>

    <div class="sender-line"><span>KLT Berlin gemeinnützige GmbH</span> | Falkenhainer Weg 14 | D-12489 Berlin</div>

    <div class="memo">
      <div class="memo__row"><div class="memo__label">To:</div><div>[Recepient Name]</div></div>
      <div class="memo__row"><div class="memo__label">From:</div><div>[Your Name]</div></div>
      <div class="memo__row"><div class="memo__label">Cc:</div><div>[Name]</div></div>
      <div class="memo__row"><div class="memo__label">Date:</div><div>[Date]</div></div>
      <div class="memo__row"><div class="memo__label">Re:</div><div>[Subject]</div></div>
    </div>

    <div class="watermark" role="img" aria-label="Faint brand emblem decoration"></div>

    <div class="body-copy">
      <p>Lorem ipsum dolor sit amet, consectetur adipiscing elit, sed do eiusmod tempor incididunt ut labore et dolore magna aliqua. Proin sagittis nisl rhoncus mattis rhoncus urna neque viverra. Sed vulputate odio ut enim blandit volutpat maecenas. Turpis in eu mi bibendum neque. Faucibus turpis in eu mi bibendum neque egestas. Massa vitae tortor condimentum lacinia quis vel eros donec. Erat pellentesque adipiscing commodo elit at imperdiet dui accumsan. Ullamcorper velit sed ullamcorper morbi. Vel facilisis volutpat est velit egestas dui. Sed lectus vestibulum mattis ullamcorper velit sed ullamcorper. Vestibulum morbi blandit cursus risus at ultrices mi tempus. Elit duis tristique sollicitudin nibh sit amet commodo nulla facilisi. Suspendisse interdum consectetur libero id. Sapien et ligula ullamcorper malesuada proin libero nunc consequat interdum. Sed vulputate odio ut enim blandit volutpat maecenas volutpat. Quis enim lobortis scelerisque fermentum dui.</p>
      <p>Praesent elementum facilisis leo vel. Enim facilisis gravida neque convallis a. Gravida arcu ac tortor dignissim convallis aenean et tortor at. Magna ac placerat vestibulum lectus mauris ultrices eros in. Bibendum est ultricies integer quis auctor elit. Odio morbi quis commodo odio aenean. Dolor sed viverra ipsum nunc aliquet bibendum enim facilisis. Iaculis urna id volutpat lacus laoreet. Posuere ac ut consequat semper viverra nam libero justo laoreet. Odio pellentesque diam volutpat commodo sed egestas egestas fringilla.</p>
      <p>Non arcu risus quis varius quam quisque id diam vel. Nunc scelerisque viverra mauris in aliquam sem fringilla. Vitae proin sagittis nisl rhoncus mattis. Pretium quam vulputate dignissim suspendisse in est ante. Sit amet est placerat in egestas erat imperdiet sed euismod. Dui ut ornare lectus sit amet est placerat in egestas. Diam phasellus vestibulum lorem sed risus ultricies tristique. In fermentum et sollicitudin ac. Blandit massa enim nec dui nunc mattis enim ut tellus. Egestas fringilla phasellus faucibus scelerisque eleifend donec pretium vulputate. Penatibus et magnis dis parturient montes.</p>
    </div>

    <div class="footer-col footer-col--contact">
      <div class="contact-row"><svg viewBox="0 0 12 12"><path d="M2.5 0.5l2 2.2-1.1 1.5c.7 1.5 1.9 2.7 3.4 3.4l1.5-1.1 2.2 2-1.3 2C5 10.2 1.8 7 .5 1.8z" fill="#a2c93a"/></svg>+49 30 55 01 24 80</div>
      <div class="contact-row"><svg viewBox="0 0 12 12"><rect x="0.6" y="2.1" width="10.8" height="7.8" fill="none" stroke="#a2c93a" stroke-width="1.2"/><path d="M0.6 2.1L6 6.6l5.4-4.5" fill="none" stroke="#a2c93a" stroke-width="1.2"/></svg>mail@klt-bildung.example</div>
      <div class="contact-row"><svg viewBox="0 0 12 12"><circle cx="6" cy="6" r="5.2" fill="none" stroke="#a2c93a" stroke-width="1.1"/><ellipse cx="6" cy="6" rx="2.2" ry="5.2" fill="none" stroke="#a2c93a" stroke-width="1"/><path d="M0.8 6h10.4" stroke="#a2c93a" stroke-width="1"/></svg>www.klt-bildung.example</div>
    </div>

    <div class="footer-col footer-col--management">
      <div class="footer-col__title">Geschäftsführer:</div>
      <div>Jorinde Paskova</div>
      <div>Lukas Drömberg</div>
    </div>

    <div class="footer-col footer-col--register">
      <div>Amtsgericht Berlin-Charlottenburg</div>
      <div>HRB 417592 B</div>
    </div>
  </div>
</body>
</html>
```